Scientific business journal infographics

We are writing a scientific article for an Academic Journal (such as the Pinecrest Strategy Quarterly, a Business Book or the Thornbury Commerce Digest). This article contains 9 infographics. We have created the graphics, and they convey the correct information and have the correct text, but they are lacking in an over-arching design and style that is clear, clean and business-like. The graphics we have created were made using a combination of Powerpoint objects and organic shapes using an AI engine. The organic shapes were deliberately made to depict the part of the process that is organic, flowing and has a level of unpredictability. As opposed to the much more rigid and linear part of the processes depicted using the Powerpoint objects.

We would like to see designs that preserve this combination of rigid process and organic process, that are clear, clean, and look well-designed and professional. These will be used in scientific business journals, and need to look like they belong there.

The designs need to have editable text, and could ideally be delivered back using a combination of images put into Powerpoint slides. We will also consider other formats, as long as we can edit them using readily available software (google cloud, MSFT 365, etc)

Font styles to use
Sans Serif

Colors

Designer to choose colors to be used in the design.

Requirements
Must have
• The sample graphics have very deliberate shapes and layouts that convey the scientific intent. Try to preserve the intent and do not reimagine the graphics or stray too far from the structure provided.

```html
<!DOCTYPE html>
<html lang="en">
<head>
<meta charset="utf-8">
<title>The Ecostructure of Strategy</title>
<link href="https://fonts.googleapis.com/css2?family=Rubik:wght@400;500;700&display=swap" rel="stylesheet">
<style>
:root{
  --page:#e1e1e1;
  --panel:#ffffff;
  --navy:#175e82;
  --navy-deep:#124b69;
  --grey:#8e99a5;
  --grey-light:#b5bfca;
  --ink:#1d1d1d;
  --frame:#e4e4e4;
  --bar-light:#a9b6c3;
  --night:#030716;
  --orb:#0b1a52;
  --orb-edge:#2d5bb5;
  --glow:#3b8be6;
}
*{margin:0;padding:0;box-sizing:border-box}
html,body{width:706px;height:1200px;overflow:hidden}
body{background:var(--page);font-family:"Rubik",Arial,sans-serif;color:var(--ink);position:relative}
.panel{position:absolute;left:34px;width:639px;background:var(--panel);overflow:hidden}
.panel::after{content:"";position:absolute;left:0;right:0;bottom:0;height:7px;
  background:linear-gradient(90deg,var(--navy) 0 565px,var(--bar-light) 565px)}
.panel--cycle{top:31px;height:360px}
.panel--ecostructure{top:413px;height:360px}
.panel--actors{top:800px;height:360px;background:var(--night)}

/* cycle */
.cycle-ring{position:absolute;left:179px;top:40px;width:280px;height:280px}
.cycle-label{position:absolute;width:200px}
.cycle-label h3{font-size:16px;font-weight:700;letter-spacing:.2px;line-height:1;margin-bottom:5px}
.cycle-label p{font-size:9.8px;line-height:12px}
.cycle-label--right{text-align:right}
.is-navy h3{color:var(--navy)}
.is-grey h3{color:var(--grey)}

/* ecostructure */
.eco-title{position:absolute;top:22px;left:0;right:0;text-align:center;font-size:30px;font-weight:700;color:var(--navy);letter-spacing:.2px;white-space:nowrap}
.eco-title span{color:var(--grey)}
.eco-links{position:absolute;left:0;top:0;width:639px;height:360px}
.eco-column{position:absolute;top:80px;width:170px;height:202px;text-align:center}
.eco-badge{position:absolute;left:55px;width:60px;height:60px}
.eco-name{position:absolute;left:0;right:0;font-size:16px;font-weight:700;letter-spacing:.3px;line-height:19px}
.eco-name--navy{color:var(--navy)}
.eco-name--grey{color:var(--grey)}
.eco-caption{position:absolute;top:297px;width:200px;text-align:center;font-size:13px;font-weight:700;line-height:16px;color:var(--ink)}
.eco-caption span{display:block;color:var(--navy)}

/* actors */
.water-scene{position:absolute;inset:0;
  background:radial-gradient(ellipse 190px 180px at 50% 58%,#2a4f86 0%,#12305e 40%,#0a1a3c 65%,transparent 100%),
  radial-gradient(ellipse 260px 200px at 50% 55%,#133066 0%,#061233 60%,var(--night) 100%)}
.actors-map{position:absolute;left:0;top:0;width:639px;height:353px}
</style>
</head>
<body>

<svg width="0" height="0" style="position:absolute">
  <defs>
    <symbol id="icon-idea" viewBox="0 0 24 24">
      <circle cx="12" cy="12" r="9.5" fill="none" stroke="currentColor" stroke-width="2.6" stroke-dasharray="2.4 1.9"/>
      <circle cx="12" cy="12" r="7.6" fill="none" stroke="currentColor" stroke-width="1.2"/>
      <path d="M12 6.6a4 4 0 0 0-2.4 7.2v1.6h4.8v-1.6A4 4 0 0 0 12 6.6z" fill="currentColor"/>
      <rect x="9.8" y="16.2" width="4.4" height="1.3" fill="currentColor"/>
    </symbol>
    <symbol id="icon-meme" viewBox="0 0 24 24">
      <rect x="3" y="9" width="18" height="10" rx="1" fill="none" stroke="currentColor" stroke-width="1.6"/>
      <rect x="9" y="20" width="6" height="1.6" fill="currentColor"/>
      <circle cx="12" cy="13" r="3.3" fill="none" stroke="currentColor" stroke-width="2.2" stroke-dasharray="1.5 1.1"/>
      <circle cx="12" cy="13" r="1.4" fill="currentColor"/>
      <path d="M7 8V4M12 8V3M17 8V4M4 6h3M17 6h3" stroke="currentColor" stroke-width="1.2" fill="none"/>
      <circle cx="7" cy="3.5" r="1" fill="currentColor"/><circle cx="17" cy="3.5" r="1" fill="currentColor"/>
    </symbol>
    <symbol id="icon-map" viewBox="0 0 24 24">
      <path d="M12 2.5a5 5 0 0 0-5 5c0 4 5 9 5 9s5-5 5-9a5 5 0 0 0-5-5z" fill="currentColor"/>
      <circle cx="12" cy="7.5" r="1.8" fill="#fff" class="pin-hole"/>
      <path d="M2 21.5l4-7h3l3 3 3-3h3l4 7z" fill="currentColor"/>
    </symbol>
    <symbol id="icon-story" viewBox="0 0 24 24">
      <path d="M9 2.5h9l3 3V19H9z" fill="none" stroke="currentColor" stroke-width="1.3"/>
      <path d="M6 4.5h9l3 3V21H6z" fill="none" stroke="currentColor" stroke-width="1.3"/>
      <path d="M11 10h5M11 12.5h5M11 15h5M11 17.5h5" stroke="currentColor" stroke-width="1"/>
      <circle cx="7" cy="15" r="4.6" fill="none" stroke="currentColor" stroke-width="1.4"/>
      <circle cx="7" cy="13.5" r="1.3" fill="currentColor"/>
      <path d="M4.8 17.6a2.3 2.3 0 0 1 4.4 0z" fill="currentColor"/>
    </symbol>
    <symbol id="icon-direction" viewBox="0 0 24 24">
      <path d="M12 2l3.5 4H13v14h-2V6H8.5z" fill="currentColor"/>
      <path d="M11 14c0-3-2-5-5-5H5V6.5L1 10l4 3.5V11h1c2 0 3 1.3 3 3v7h2z" fill="currentColor"/>
      <path d="M13 14h5v2.5l4-3.5-4-3.5V12h-5z" fill="currentColor"/>
    </symbol>
    <symbol id="icon-decision" viewBox="0 0 24 24">
      <circle cx="5.5" cy="4.5" r="3" fill="currentColor"/>
      <path d="M4.2 4.5l1 1 2-2" stroke="#fff" stroke-width="0.9" fill="none" class="mark"/>
      <circle cx="18.5" cy="4.5" r="3" fill="currentColor"/>
      <path d="M17.2 3.2l2.6 2.6M19.8 3.2l-2.6 2.6" stroke="#fff" stroke-width="0.9" class="mark"/>
      <path d="M5.5 7.5v3h3M18.5 7.5v3h-3" stroke="currentColor" stroke-width="1" fill="none"/>
      <circle cx="12" cy="11" r="3.2" fill="currentColor"/>
      <path d="M5.5 22a6.5 6.5 0 0 1 13 0z" fill="currentColor"/>
      <circle cx="18" cy="18" r="3" fill="none" stroke="currentColor" stroke-width="1.8" stroke-dasharray="1.3 1"/>
    </symbol>
    <symbol id="icon-actor" viewBox="0 0 24 24">
      <rect x="5" y="1.5" width="14" height="9" fill="currentColor"/>
      <path d="M12 3.5l1 2.1 2.2.2-1.7 1.4.6 2.1-2.1-1.2-2.1 1.2.6-2.1-1.7-1.4 2.2-.2z" fill="#0b1a52"/>
      <rect x="4" y="11.5" width="16" height="2" fill="currentColor"/>
      <path d="M6 14l12 9M18 14L6 23" stroke="currentColor" stroke-width="1.6"/>
    </symbol>
    <symbol id="icon-action" viewBox="0 0 24 24">
      <circle cx="15" cy="4.5" r="2.2" fill="currentColor"/>
      <path d="M13.5 7.5l-4 1.5-2 3M13.5 7.5l-2 6 3 3-1 5M11.5 13.5l-3 3-3 0M13.5 9l3 2.5 3-1" stroke="currentColor" stroke-width="2" fill="none" stroke-linecap="round"/>
      <path d="M1 10h5M2 13h4M1 16h3" stroke="currentColor" stroke-width="1"/>
      <circle cx="20" cy="4" r="2.4" fill="none" stroke="currentColor" stroke-width="1.6" stroke-dasharray="1.2 0.9"/>
    </symbol>
    <symbol id="icon-artifact" viewBox="0 0 24 24">
      <rect x="7" y="2" width="14" height="11" fill="none" stroke="currentColor" stroke-width="1.4"/>
      <path d="M11.5 5.5l-1.5 1.5 1.5 1.5M16.5 5.5l1.5 1.5-1.5 1.5M14.8 4.8l-1.6 4.4" stroke="currentColor" stroke-width="1" fill="none"/>
      <rect x="2" y="14" width="9" height="4" fill="none" stroke="currentColor" stroke-width="1.4"/>
      <rect x="2" y="18" width="9" height="4" fill="none" stroke="currentColor" stroke-width="1.4"/>
      <rect x="12" y="16" width="9" height="6" fill="currentColor"/>
      <path d="M5 16h3M5 20h3" stroke="currentColor" stroke-width="1"/>
    </symbol>
    <linearGradient id="grad-grey" x1="0" y1="0" x2="1" y2="1">
      <stop offset="0" stop-color="#8c97a3"/><stop offset="1" stop-color="#c2cad3"/>
    </linearGradient>
    <linearGradient id="grad-badge-navy" x1="0" y1="0" x2="1" y2="1">
      <stop offset="0" stop-color="#1e86b5"/><stop offset="1" stop-color="#104764"/>
    </linearGradient>
    <linearGradient id="grad-badge-grey" x1="0" y1="0" x2="1" y2="1">
      <stop offset="0" stop-color="#c9d0d8"/><stop offset="1" stop-color="#8a949f"/>
    </linearGradient>
    <radialGradient id="grad-orb" cx="0.5" cy="0.35" r="0.7">
      <stop offset="0" stop-color="#14287a"/><stop offset="1" stop-color="#050b2b"/>
    </radialGradient>
    <filter id="soft-shadow" x="-20%" y="-20%" width="140%" height="140%">
      <feDropShadow dx="0" dy="2" stdDeviation="4" flood-color="#000" flood-opacity="0.18"/>
    </filter>
  </defs>
</svg>

<!-- Six-part cycle -->
<section class="panel panel--cycle">
  <svg class="cycle-ring" viewBox="0 0 280 280">
    <circle cx="140" cy="140" r="137" fill="#fff" filter="url(#soft-shadow)"/>
    <g stroke="#fff" stroke-width="4">
      <path class="segment segment--ideas" d="M140 10A130 130 0 0 1 252.6 75L193.7 109A62 62 0 0 0 140 78Z" fill="var(--navy)"/>
      <path class="segment segment--memes" d="M252.6 75A130 130 0 0 1 252.6 205L193.7 171A62 62 0 0 0 193.7 109Z" fill="url(#grad-grey)"/>
      <path class="segment segment--maps" d="M252.6 205A130 130 0 0 1 140 270L140 202A62 62 0 0 0 193.7 171Z" fill="var(--navy)"/>
      <path class="segment segment--stories" d="M140 270A130 130 0 0 1 27.4 205L86.3 171A62 62 0 0 0 140 202Z" fill="url(#grad-grey)"/>
      <path class="segment segment--direction" d="M27.4 205A130 130 0 0 1 27.4 75L86.3 109A62 62 0 0 0 86.3 171Z" fill="var(--navy)"/>
      <path class="segment segment--decisions" d="M27.4 75A130 130 0 0 1 140 10L140 78A62 62 0 0 0 86.3 109Z" fill="url(#grad-grey)"/>
    </g>
    <g class="puzzle-knobs" fill="var(--navy)">
      <circle cx="128.2" cy="43.7" r="12"/>
      <circle cx="229.3" cy="102.1" r="12"/>
      <circle cx="229.3" cy="177.9" r="12"/>
      <circle cx="128.2" cy="236.3" r="12"/>
      <circle cx="62.5" cy="198.4" r="12"/>
      <circle cx="62.5" cy="81.6" r="12"/>
    </g>
    <g class="step-ring" stroke="#fff" stroke-width="3">
      <path d="M140 83A57 57 0 0 1 189.4 111.5L172 121.5A37 37 0 0 0 140 103Z" fill="var(--navy)"/>
      <path d="M189.4 111.5A57 57 0 0 1 189.4 168.5L172 158.5A37 37 0 0 0 172 121.5Z" fill="var(--grey-light)"/>
      <path d="M189.4 168.5A57 57 0 0 1 140 197L140 177A37 37 0 0 0 172 158.5Z" fill="var(--navy)"/>
      <path d="M140 197A57 57 0 0 1 90.6 168.5L108 158.5A37 37 0 0 0 140 177Z" fill="var(--grey-light)"/>
      <path d="M90.6 168.5A57 57 0 0 1 90.6 111.5L108 121.5A37 37 0 0 0 108 158.5Z" fill="var(--navy)"/>
      <path d="M90.6 111.5A57 57 0 0 1 140 83L140 103A37 37 0 0 0 108 121.5Z" fill="var(--grey-light)"/>
    </g>
    <g class="step-numbers" fill="#fff" font-family="Rubik, Arial, sans-serif" font-size="11" font-weight="500" text-anchor="middle" dominant-baseline="central">
      <text transform="translate(116.5 99.3) rotate(-30)">01</text>
      <text transform="translate(163.5 99.3) rotate(30)">02</text>
      <text transform="translate(187 140) rotate(90)">03</text>
      <text transform="translate(163.5 180.7) rotate(-30)">04</text>
      <text transform="translate(116.5 180.7) rotate(30)">05</text>
      <text transform="translate(93 140) rotate(-90)">06</text>
    </g>
    <g class="segment-icons" color="#fff">
      <use href="#icon-idea" x="170" y="40" width="36" height="36"/>
      <use href="#icon-meme" x="217" y="122" width="36" height="36"/>
      <use href="#icon-map" x="170" y="204" width="36" height="36"/>
      <use href="#icon-story" x="74" y="204" width="36" height="36"/>
      <use href="#icon-direction" x="26" y="122" width="36" height="36"/>
      <use href="#icon-decision" x="74" y="40" width="36" height="36"/>
    </g>
  </svg>

  <div class="cycle-label cycle-label--right is-grey" style="left:3px;top:26px">
    <h3>DECISIONS</h3>
    <p>Execution of critical<br>decision-making<br>processes.</p>
  </div>
  <div class="cycle-label is-navy" style="left:434px;top:26px">
    <h3>IDEAS</h3>
    <p>Conceptualization of<br>individual ideas and<br>micro strategies.</p>
  </div>
  <div class="cycle-label is-grey" style="left:472px;top:138px;width:165px">
    <h3>MEMES</h3>
    <p style="line-height:11.2px">Integration into organizational<br>lexicon and behavioural<br>patterns, incl. social cues<br>signalling the do’s and don’ts<br>of what is deemed as “acceptable”<br>or “normal” behaviour</p>
  </div>
  <div class="cycle-label cycle-label--right is-navy" style="left:-38px;top:149px">
    <h3>DIRECTION</h3>
    <p>Provision of<br>guidance and<br>directives.</p>
  </div>
  <div class="cycle-label cycle-label--right is-grey" style="left:3px;top:277px">
    <h3>STORIES</h3>
    <p>Creation of coherent<br>and adaptable<br>narratives.</p>
  </div>
  <div class="cycle-label is-navy" style="left:436px;top:277px">
    <h3>MAPS</h3>
    <p>Development of<br>future state<br>roadmaps.</p>
  </div>
</section>

<!-- Ecostructure -->
<section class="panel panel--ecostructure">
  <h2 class="eco-title">THE ECOSTRUCTURE <span>OF STRATEGY</span></h2>

  <svg class="eco-links" viewBox="0 0 639 360" fill="none" stroke="var(--frame)" stroke-width="2.5">
    <path d="M199 150V97a17 17 0 0 0-17-17H47a17 17 0 0 0-17 17v168a17 17 0 0 0 17 17h135a17 17 0 0 0 17-17V178"/>
    <path d="M235 125V97a17 17 0 0 1 17-17h135a17 17 0 0 1 17 17v53M404 178v87a17 17 0 0 1-17 17H252a17 17 0 0 1-17-17V150"/>
    <path d="M439 125V97a17 17 0 0 1 17-17h136a17 17 0 0 1 17 17v168a17 17 0 0 1-17 17H456a17 17 0 0 1-17-17V150"/>
    <circle cx="199" cy="164" r="7" fill="#fff"/>
    <circle cx="404" cy="164" r="7" fill="#fff"/>
    <path d="M199 200v-5a12 12 0 0 1 12-12h18"/>
    <path d="M404 200v-5a12 12 0 0 1 12-12h18"/>
    <path d="M235 172l10 11-10 11z" fill="var(--frame)" stroke="none"/>
    <path d="M439 172l10 11-10 11z" fill="var(--frame)" stroke="none"/>
  </svg>

  <div class="eco-column" style="left:30px">
    <svg class="eco-badge" style="top:12px" viewBox="0 0 60 60"><circle cx="30" cy="30" r="29" fill="#fff" stroke="var(--navy)" stroke-width="1"/><circle cx="30" cy="30" r="27" fill="url(#grad-badge-navy)"/><use href="#icon-idea" x="15" y="15" width="30" height="30" color="#fff"/></svg>
    <div class="eco-name eco-name--navy" style="top:74px">IDEAS</div>
    <svg class="eco-badge" style="top:106px" viewBox="0 0 60 60"><circle cx="30" cy="30" r="29" fill="#fff" stroke="var(--grey)" stroke-width="1"/><circle cx="30" cy="30" r="27" fill="url(#grad-badge-grey)"/><use href="#icon-meme" x="15" y="15" width="30" height="30" color="#fff"/></svg>
    <div class="eco-name eco-name--grey" style="top:168px">MEMES</div>
  </div>
  <div class="eco-column" style="left:235px">
    <svg class="eco-badge" style="top:12px" viewBox="0 0 60 60"><circle cx="30" cy="30" r="29" fill="#fff" stroke="var(--navy)" stroke-width="1"/><circle cx="30" cy="30" r="27" fill="url(#grad-badge-navy)"/><use href="#icon-map" x="15" y="15" width="30" height="30" color="#fff"/></svg>
    <div class="eco-name eco-name--navy" style="top:74px">MAPS</div>
    <svg class="eco-badge" style="top:106px" viewBox="0 0 60 60"><circle cx="30" cy="30" r="29" fill="#fff" stroke="var(--grey)" stroke-width="1"/><circle cx="30" cy="30" r="27" fill="url(#grad-badge-grey)"/><use href="#icon-story" x="15" y="15" width="30" height="30" color="#fff"/></svg>
    <div class="eco-name eco-name--grey" style="top:168px">STORIES</div>
  </div>
  <div class="eco-column" style="left:439px">
    <svg class="eco-badge" style="top:12px" viewBox="0 0 60 60"><circle cx="30" cy="30" r="29" fill="#fff" stroke="var(--navy)" stroke-width="1"/><circle cx="30" cy="30" r="27" fill="url(#grad-badge-navy)"/><use href="#icon-direction" x="15" y="15" width="30" height="30" color="#fff"/></svg>
    <div class="eco-name eco-name--navy" style="top:74px">DIRECTIONS</div>
    <svg class="eco-badge" style="top:106px" viewBox="0 0 60 60"><circle cx="30" cy="30" r="29" fill="#fff" stroke="var(--grey)" stroke-width="1"/><circle cx="30" cy="30" r="27" fill="url(#grad-badge-grey)"/><use href="#icon-decision" x="15" y="15" width="30" height="30" color="#fff"/></svg>
    <div class="eco-name eco-name--grey" style="top:168px">DECISIONS</div>
  </div>

  <div class="eco-caption" style="left:15px"><span>ECOSYSTEM OF</span>EMERGENCE</div>
  <div class="eco-caption" style="left:220px"><span>ECOSYSTEM OF</span>(RE-/DE-) STRUCTURING</div>
  <div class="eco-caption" style="left:424px"><span>ECOSYSTEM OF</span>REIFICATION</div>
</section>

<!-- Actors, actions, artifacts -->
<section class="panel panel--actors">
  <div class="water-scene" role="img" aria-label="Swirling deep-blue water vortex surrounding the strategy cycle"></div>
  <svg class="actors-map" viewBox="0 0 639 353">
    <circle cx="319" cy="197" r="92" fill="rgba(4,10,36,0.55)" stroke="#c9d6e6" stroke-width="2.5"/>
    <circle cx="319" cy="197" r="88" fill="none" stroke="#1c2f6b" stroke-width="2"/>
    <path d="M397 150l5 15 4-14z" fill="#c9d6e6"/>
    <path d="M305 288l-14 1 12 7z" fill="#c9d6e6"/>
    <path d="M232 165l-2-15 9 12z" fill="#c9d6e6"/>

    <g color="var(--glow)" fill="#fff" font-family="Rubik, Arial, sans-serif" font-size="11" font-weight="500" text-anchor="middle">
      <use href="#icon-idea" x="308" y="126" width="22" height="22"/><text x="319" y="158">Ideas</text>
      <use href="#icon-decision" x="251" y="150" width="22" height="22"/><text x="262" y="184">Decision</text>
      <use href="#icon-meme" x="369" y="152" width="22" height="22"/><text x="380" y="186">Memes</text>
      <use href="#icon-direction" x="251" y="198" width="22" height="22"/><text x="262" y="232">Direction</text>
      <use href="#icon-map" x="369" y="200" width="22" height="22"/><text x="380" y="234">Maps</text>
      <use href="#icon-story" x="305" y="233" width="24" height="24"/><text x="317" y="272">Stories</text>
    </g>

    <g class="orbs" font-family="Rubik, Arial, sans-serif" font-size="16" font-weight="700" fill="#fff" text-anchor="middle">
      <circle cx="319" cy="72" r="46" fill="url(#grad-orb)" stroke="var(--orb-edge)" stroke-width="3"/>
      <use href="#icon-actor" x="301" y="40" width="36" height="36" color="#fff"/>
      <text x="319" y="96">Actors</text>
      <circle cx="204" cy="268" r="46" fill="url(#grad-orb)" stroke="var(--orb-edge)" stroke-width="3"/>
      <use href="#icon-action" x="186" y="236" width="36" height="36" color="#fff"/>
      <text x="204" y="292">Actions</text>
      <circle cx="435" cy="268" r="46" fill="url(#grad-orb)" stroke="var(--orb-edge)" stroke-width="3"/>
      <use href="#icon-artifact" x="418" y="238" width="34" height="34" color="#fff"/>
      <text x="435" y="292">Artifacts</text>
    </g>
  </svg>
</section>

</body>
</html>
```